Flyer-Design für Prozessfinanzierungsfirma
Zielgruppe
Wir sind eine Prozessfinanzierungsfirma. im Versicherungsbereich die größte Österreichs mit mehr als 50.000 Klienten und unser neues Projekt ist die Prozessfinanzierung von Patienten die durch einen Kunstfehler (Fehler von Ärzten) auf Schadenersatz klagen wollen aber nicht die Finanziellen Möglichkeiten haben.
Aufgabenstellung
Folder soll eine DIN A4 Doppelseite sein (also 4 A4 Seiten)
plus extra ein A4 Einlage Blatt Fragebogen fix vorgegebene Fragen.
#604132 Dieser Folder ist für die gleiche Firma im Bereich Versicherungen
www.heilirrtum-beispiel.at. TEXTE und DESIGN - FARBEN und INHALTE von dieser Homepage übernehmen
die Seite www.schutzbrief-muster.at ist die gleiche Prozessfinanzierungsfirma - hier gibt es bereits einen Folder. Ich lade diesen hoch...
Diese Fragen sind unbedingt 1:1 zu übernehmen für das Einlageblatt :
o Was waren meine Erkrankungen vor der Behandlung, inkl. Dauermedikation?
o Warum ging ich zum Arzt?
o Was hat mir der Arzt empfohlen?
o Wurde ich über die unterschiedlichen Behandlungsmöglichkeiten aufgeklärt?
o Was wollte ich haben?
o Was wurde gemacht?
o Was hat der Arzt aus meiner Sicht falsch gemacht?
o Was wurde als weiterer Behandlungsweg empfohlen?
o Habe ich den Arzt mit meinem Problem konfrontiert?
o Wie hat mein Arzt darauf reagiert?
o Was ist jetzt genau schlechter als vorher?
Bei dem A4 Einlageblatt sollen auf der Vorderseite und der halben Rückseite diese Fragen mit entsprechendem Platz für den Text zum ausfüllen erscheinen und die untere Hälfte der 2. Seite mit einem kurzen Slogan nochmal auf unsere Leistung aufmerksam machen - ein Feld in Kreditkartengrösse für den Empfehlungsbgeber weiss zum einkleben einer Karte freibleiben und die Firmendaten (siehe Homepage) mit Anschrift, Telefonnummer und e-mailadresse angegeben sein

```html
<!DOCTYPE html>
<html lang="de">
<head>
<meta charset="utf-8">
<title>Folder Prozessfinanzierung – Behandlungsfehler</title>
<link href="https://fonts.googleapis.com/css2?family=Ubuntu:wght@300;400;500;700&display=swap" rel="stylesheet">
<style>
:root{
  --red:#8a1912;
  --brown:#6a3a2e;
  --rose:#c9a4a2;
  --blush:#e9dcdc;
  --ink:#3a3333;
  --paper:#ffffff;
  --rule:#d9d2d2;
}
*{box-sizing:border-box;margin:0;padding:0}
html,body{width:1200px;height:849px;overflow:hidden;background:#fff}
body{position:relative;font-family:"Ubuntu",sans-serif;color:var(--ink)}
.page{position:absolute;background:var(--paper);overflow:hidden;box-shadow:0 3px 8px rgba(0,0,0,.18)}
.page svg.bg{position:absolute;inset:0;width:100%;height:100%}
.abs{position:absolute}
.brand{position:absolute;display:flex;align-items:center;gap:5px;font-weight:500;font-size:8.5px;letter-spacing:.4px;color:var(--ink)}
.brand i{display:block;width:16px;height:16px;border:1.4px solid var(--ink)}
.headline{font-weight:300;color:#fff;font-size:11.5px;line-height:1.2}
.title{font-weight:400;color:var(--red);font-size:9.5px;line-height:1.15}
.copy{font-size:4.3px;line-height:1.55;font-weight:300;color:var(--ink)}
.copy b{font-weight:700}
.copy.white{color:#fff}
.copy ul,.copy ol{list-style:none}
.copy li{position:relative;padding-left:5px}
.copy ul li::before{content:"•";position:absolute;left:0}
.link{font-size:4.4px;font-weight:700;color:var(--red)}
.q{position:absolute;left:16px;right:14px;font-size:4.5px;font-weight:700;color:var(--red)}
.q .lines{margin-top:5px;height:34px;background:repeating-linear-gradient(to bottom,transparent 0 8.2px,var(--rule) 8.2px 8.8px)}
.card-slot{position:absolute;background:#fff;border-radius:4px;font-size:4.5px;font-weight:700;color:var(--ink);padding:5px}
</style>
</head>
<body>

<svg width="0" height="0" style="position:absolute">
  <defs>
    <linearGradient id="tone-clinic" x1="0" y1="0" x2="1" y2="1">
      <stop offset="0" stop-color="#9fb0ae"/><stop offset=".55" stop-color="#5f7371"/><stop offset="1" stop-color="#a0584a"/>
    </linearGradient>
    <linearGradient id="tone-team" x1="0" y1="0" x2="1" y2="1">
      <stop offset="0" stop-color="#b8bcc4"/><stop offset=".5" stop-color="#6d6a70"/><stop offset="1" stop-color="#3f4a63"/>
    </linearGradient>
    <linearGradient id="tone-desk" x1="0" y1="0" x2="1" y2="1">
      <stop offset="0" stop-color="#3b5d72"/><stop offset=".4" stop-color="#c7ccd0"/><stop offset="1" stop-color="#eceef0"/>
    </linearGradient>
    <linearGradient id="tone-glove" x1="0" y1="0" x2="1" y2="1">
      <stop offset="0" stop-color="#c9c6c0"/><stop offset=".6" stop-color="#ebe7e1"/><stop offset="1" stop-color="#cfb0a8"/>
    </linearGradient>
    <linearGradient id="tone-xray" x1="0" y1="0" x2="1" y2="1">
      <stop offset="0" stop-color="#6f7d95"/><stop offset=".5" stop-color="#26324a"/><stop offset="1" stop-color="#8b8f9e"/>
    </linearGradient>
    <linearGradient id="tone-tools" x1="0" y1="0" x2="1" y2="1">
      <stop offset="0" stop-color="#8ea0ab"/><stop offset=".6" stop-color="#b6c1c8"/><stop offset="1" stop-color="#d8cfc7"/>
    </linearGradient>
  </defs>
</svg>

<!-- Cover -->
<section class="page cover" style="left:55px;top:46px;width:257px;height:363px">
  <svg class="bg" viewBox="0 0 257 363" preserveAspectRatio="none">
    <rect x="0" y="209" width="257" height="154" fill="var(--blush)"/>
    <polygon points="0,63 147,63 172,120 0,120" fill="var(--red)"/>
    <polygon points="172,120 257,120 257,183 205,209 150,209" fill="var(--brown)" opacity=".9"/>
    <polygon points="0,120 172,120 205,209 0,209" fill="url(#tone-clinic)" role="img" aria-label="Foto: Blutdruckmessung mit Stethoskop und Patientenakte"/>
    <polygon points="150,183 257,183 257,249 124,249" fill="var(--red)"/>
    <polygon points="118,249 132,249 92,363 80,363" fill="var(--rose)"/>
    <polygon points="132,249 257,249 257,363 92,363" fill="url(#tone-team)" role="img" aria-label="Foto: Ärzte betrachten gemeinsam ein Röntgenbild"/>
  </svg>
  <div class="brand" style="left:25px;top:30px"><i></i>NORVIA PROZESSHILFE</div>
  <h1 class="headline abs" style="left:25px;top:70px">Sie haben einen<br>Behandlungsfehler<br>erlitten?</h1>
  <p class="copy white abs" style="left:150px;top:196px;width:100px;text-align:center">Eine Klageführung gegen Ärzte ist in der Praxis schwierig und teuer, Rechtsschutzversicherungen sind meist nicht vorhanden oder lehnen eine Deckung in der erforderlichen Höhe ab.<br><b>Genau hier helfen wir Ihnen weiter!</b></p>
  <h2 class="title abs" style="left:25px;top:222px">Dürfen wir Ihnen<br>helfen?</h2>
  <p class="copy abs" style="left:25px;top:249px;width:86px">Wir helfen Ihnen bei der <b>Klageführung gegen Ihren Arzt</b> weiter und übernehmen Ihr gesamtes Prozessrisiko! Wie das geht erfahren Sie hier und auf unserer Webseite.</p>
  <p class="link abs" style="left:25px;top:286px">www.heilirrtum-beispiel.at</p>
</section>

<!-- Inner spread -->
<section class="page spread" style="left:344px;top:45px;width:515px;height:364px">
  <svg class="bg" viewBox="0 0 515 364" preserveAspectRatio="none">
    <polygon points="240,144 515,144 515,364 257,364" fill="var(--blush)"/>
    <polygon points="253,0 515,0 515,144 240,144" fill="url(#tone-desk)" role="img" aria-label="Foto: Stethoskop auf einem Terminkalender"/>
    <polygon points="0,144 195,144 210,195 0,195" fill="var(--red)"/>
    <polygon points="195,144 240,144 253,195 210,195" fill="var(--brown)"/>
    <polygon points="240,144 257,144 257,195 253,195" fill="var(--rose)"/>
    <polygon points="133,195 253,195 257,364 133,364" fill="url(#tone-glove)" role="img" aria-label="Foto: Hand im Handschuh hält eine Blutprobe"/>
    <polygon points="237,195 257,195 257,364 270,364" fill="var(--rose)" opacity=".55"/>
    <polygon points="257,290 282,364 257,364" fill="var(--rose)"/>
    <line x1="257" y1="0" x2="257" y2="364" stroke="rgba(0,0,0,.12)" stroke-width=".6"/>
  </svg>
  <h2 class="title abs" style="left:24px;top:23px">Willkommen bei heilirrtum-beispiel.at</h2>
  <p class="abs" style="left:24px;top:36px;font-size:4.4px;color:var(--red)">Ein Unternehmen der Norvia Prozesshilfe GmbH</p>
  <p class="copy abs" style="left:24px;top:59px;width:98px">Ärztliche Behandlungsfehler - Kunstfehler - Arztfehler können passieren! Aber wie kann man seine erlittenen Schmerzen zumindest durch einen Geldanspruch ausgleichen lassen? Wer übernimmt dafür das Risiko? <b>Eine Klageführung gegen Ärzte</b> ist in der Praxis schwierig und teuer, Rechtsschutzversicherungen sind meist nicht vorhanden oder lehnen eine Deckung in der</p>
  <p class="copy abs" style="left:133px;top:59px;width:100px">erforderlichen Höhe ab.<br><b>Genau hier helfen wir Ihnen weiter! Wir übernehmen Ihr gesamtes Prozessrisiko!</b> Wir empfehlen Ihnen nach einer ersten Analyse Ihres Falles einen spezialisierten Rechtsanwalt, der mit Ihnen Ihren Fall bespricht und sodann Ihren Arzt oder das Spital mit Ihrer Forderung (meistens Schmerzensgeld) konfrontiert.</p>
  <p class="copy white abs" style="left:20px;top:153px;width:168px">Für die Tragung dieses Risikos <b>vereinbaren Sie mit uns eine Erfolgsbeteiligung.</b> Wenn wir für Sie also nichts „erreichen“ hat es Sie nichts gekostet und wir tragen sämtliche Kosten. „Wir sitzen somit in einem Boot“ – und begleiten Sie vertrauensvoll in Ihrer schwierigen Situation.</p>
  <h3 class="abs" style="left:24px;top:208px;font-size:4.6px;font-weight:700;color:var(--red)">Was kann der verletzte Patient fordern?</h3>
  <div class="copy abs" style="left:24px;top:219px;width:100px">
    <p>Erleidet nun ein Patient durch ein pflichtwidriges Verhalten eines Arztes (Behandlungsfehler) einen Schaden (z.B. Schmerzen), so kann der Verletzte dafür einen Geldbetrag fordern.<br>Man kann diese Forderungen wie folgt einteilen:</p>
    <ul style="margin-top:2px;line-height:2.1">
      <li>Schmerzensgeld für erlittene Schmerzen</li>
      <li>Anspruch für seelische Schmerzen</li>
      <li>Weitere Behandlungen</li>
      <li>Heimhilfe oder eine weitere Betreuung</li>
      <li>Umbau der Wohnung</li>
      <li>Verunstaltungsentschädigung</li>
      <li>Folgeschäden</li>
    </ul>
  </div>
  <h2 class="title abs" style="left:281px;top:157px">Das tun wir für Sie!</h2>
  <div class="copy abs" style="left:281px;top:173px;width:205px">
    <p>Wir helfen Ihnen in dieser Situation schnell und unbürokratisch weiter. Wir übernehmen sämtliche anfallenden Kosten:</p>
    <ul style="margin-top:2px">
      <li>Anwaltliches Erstgespräch und Folgegespräche</li>
      <li>Aufforderungsschreiben gegen die Versicherung</li>
      <li>Verhandlungen mit der Versicherung</li>
      <li>Klage gegen die Versicherung</li>
      <li>Kosten von Gutachten</li>
      <li>Kosten der Gerichtsverhandlungen</li>
      <li>Kosten von Berufungen und Revisionen</li>
    </ul>
    <p style="margin-top:5px">Als Gegenleistung dafür teilen Sie mit uns den erstrittenen Betrag. <b>Sie haben daher keinerlei Risiko.</b></p>
    <p style="margin-top:5px;text-align:center">Sobald Sie uns Ihre benötigten Daten online hochgeladen oder ganz einfach per Post geschickt haben erfolgt eine erste Durchsicht Ihrer Akten. Sollte alles vollständig und der Akt erfolgversprechend sein, schlagen wir Ihnen einen unserer spezialisierten Rechtsanwälte vor. Diese erörtern mit Ihnen Ihren Fall und leiten die erforderlichen Schritte ein.</p>
    <p style="margin-top:5px;text-align:center"><b>Gerne helfen wir Ihnen, Sie haben nun einen starken Partner, der Ihnen eine Verhandlung gegen die meist übermächtigen Spitäler oder Ärzte auf Augenhöhe ermöglicht!</b></p>
  </div>
</section>

<!-- Back page -->
<section class="page back" style="left:907px;top:46px;width:257px;height:363px">
  <svg class="bg" viewBox="0 0 257 363" preserveAspectRatio="none">
    <rect x="0" y="120" width="257" height="243" fill="var(--blush)"/>
    <polygon points="84,120 102,63 257,63 257,120" fill="url(#tone-xray)" role="img" aria-label="Foto: Hand hält ein Röntgenbild der Wirbelsäule"/>
    <polygon points="0,120 101,120 84,203 0,203" fill="url(#tone-tools)" role="img" aria-label="Foto: medizinische Instrumente und Klemmbrett auf dem Tisch"/>
    <polygon points="101,120 111,120 94,203 84,203" fill="var(--rose)" opacity=".7"/>
    <polygon points="0,203 117,203 150,363 0,363" fill="var(--red)"/>
  </svg>
  <div class="brand" style="left:109px;top:30px"><i></i>NORVIA PROZESSHILFE</div>
  <h2 class="headline abs" style="left:16px;top:233px;font-size:9.5px;font-weight:400">Kontakt</h2>
  <p class="copy white abs" style="left:16px;top:254px;width:90px"><b>Norvia Prozesshilfe GmbH</b><br>FN 000000x<br>UID: ATU00000000<br>Musterplatz 12<br>1010 Wien<br>Tel: +43 (0)1/555 10 10<br>Fax: +43 (0)1/555 10 10-10<br>office@heilirrtum-beispiel.at</p>
  <p class="copy white abs" style="left:16px;top:310px"><b>www.heilirrtum-beispiel.at</b></p>
  <h2 class="title abs" style="left:127px;top:139px;font-size:8px;width:120px">Wir helfen Ihnen erfolgreich – Schritt für Schritt!</h2>
  <div class="copy abs" style="left:114px;top:171px;width:136px">
    <p style="text-align:center">Jeder einzelne Schritt ist transparent und für Sie einsehbar. Sie erhalten nach Einreichung Ihrer Daten einen Online-Zugang zu Ihrem Akt.</p>
    <p style="text-align:center;margin-top:4px">Dort können Sie jederzeit fehlende Unterlagen hochladen und den jeweiligen Staus Ihres Aktes einsehen. Es gibt folgende Schritte:</p>
    <ol>
      <li style="margin-left:10px">1. Akt erfassen (online oder über beiliegendes Formular)</li>
      <li style="margin-left:15px">2. Vereinbarung für Kostenübernahme erhalten</li>
      <li style="margin-left:18px">3. Wir überprüfen Ihre Daten</li>
      <li style="margin-left:21px">4. Akt in Bearbeitung bei Rechtsanwalt</li>
      <li style="margin-left:24px">5. Forderung an Arzt gestellt</li>
      <li style="margin-left:27px">6. Vergleichsverhandlungen im Laufen</li>
      <li style="margin-left:30px">7. Klage eingebracht</li>
      <li style="margin-left:33px">8. Vergleich erzielt / Klage erfolgreich samt Betragshöhe</li>
    </ol>
    <p style="margin:5px 0 0 38px;text-align:center"><b>Mehr Infos erhalten Sie auf unserer Webseite:</b></p>
  </div>
  <p class="link abs" style="left:150px;top:316px">www.heilirrtum-beispiel.at</p>
</section>

<!-- Questionnaire front -->
<section class="page form-front" style="left:326px;top:457px;width:259px;height:366px">
  <svg class="bg" viewBox="0 0 259 366" preserveAspectRatio="none">
    <polygon points="215,0 255,0 233,54 196,54" fill="var(--blush)"/>
    <polygon points="0,16 200,16 218,54 0,54" fill="var(--red)"/>
    <polygon points="200,16 215,16 233,54 202,54" fill="var(--brown)"/>
  </svg>
  <h1 class="headline abs" style="left:16px;top:21px;font-size:10px;font-weight:400">Fragebogen</h1>
  <p class="copy white abs" style="left:16px;top:36px;width:180px">Beantorten Sie folgende Fragen und wir senden Ihnen schnellstmöglich eine unverbindliche Vereinbarung für die Kostenübernahme zu.</p>
  <div class="q" style="top:65px">Was waren meine Erkrankungen vor der Behandlung, inkl. Dauermedikation?<div class="lines"></div></div>
  <div class="q" style="top:115px">Warum ging ich zum Arzt?<div class="lines"></div></div>
  <div class="q" style="top:163px">Was hat mir der Arzt empfohlen?<div class="lines"></div></div>
  <div class="q" style="top:212px">Wurde ich über die unterschiedlichen Behandlungsmöglichkeiten aufgeklärt?<div class="lines"></div></div>
  <div class="q" style="top:260px">Was wollte ich haben?<div class="lines"></div></div>
  <div class="q" style="top:308px">Was wurde gemacht?<div class="lines"></div></div>
</section>

<!-- Questionnaire back -->
<section class="page form-back" style="left:620px;top:455px;width:254px;height:360px">
  <svg class="bg" viewBox="0 0 254 360" preserveAspectRatio="none">
    <rect x="0" y="280" width="254" height="80" fill="var(--blush)"/>
    <polygon points="8,280 35,280 22,318" fill="var(--rose)"/>
    <polygon points="22,318 45,360 6,360" fill="#fff"/>
  </svg>
  <div class="q" style="top:14px">Was hat der Arzt aus meiner Sicht falsch gemacht?<div class="lines"></div></div>
  <div class="q" style="top:69px">Was wurde als weiterer Behandlungsweg empfohlen?<div class="lines"></div></div>
  <div class="q" style="top:124px">Habe ich den Arzt mit meinem Problem konfrontiert?<div class="lines"></div></div>
  <div class="q" style="top:176px">Wie hat mein Arzt darauf reagiert?<div class="lines"></div></div>
  <div class="q" style="top:226px">Was ist jetzt genau schlechter als vorher?<div class="lines"></div></div>
  <h2 class="title abs" style="left:43px;top:287px">Kontakt</h2>
  <p class="copy abs" style="left:45px;top:302px;width:90px;text-align:center"><b>Norvia Prozesshilfe GmbH</b><br>UID: ATU00000000<br>Musterplatz 12, 1010 Wien<br>Tel: +43 (0)1/555 10 10<br>Fax: +43 (0)1/555 10 10-10<br>office@heilirrtum-beispiel.at<br><b>www.heilirrtum-beispiel.at</b></p>
  <div class="card-slot" style="left:136px;top:287px;width:104px;height:58px">Empfehlungsbgeber</div>
</section>

</body>
</html>
```